Medical Software Informational Flyer and Website Design

Our company, Copper Vale Systems, is launching a new product, the Copper Vale Clinic Flow Platform. It is a software suite that will increase the productivity and volume of a LASIK practice.

We want this flyer to be a companion to our big reveal presentation at OPX and NVCSE; it's primary purpose is to inform potential clients on the many ways this software will help their practice. It is also obviously a promotional material. Because it is a companion to our presentation, we feel that it is acceptable for the flyer to contain much more text than would normally be reasonable in a flyer; it will go into more detail about the 12 major selling points of our software than our presentation time will allow. Having said that, however, we still want there to be "breathing room" for the design and the viewer's eyes.

We have uploaded our logo, both in full color and in white with no background (often used for watermarks, but certainly not restricted for that use alone). Our logo should be accompanied by either "Copper Vale Systems" or "Copper Vale" using the Trajan Pro font (unoriginal, we know, but it's what we've chosen). We have included a color palette that compliments our logo, but designs are not limited to that palette (for example, we have found a pink (#cc1448) that compliments the palette and that we have used in the presentation).

We have also uploaded a PSD that includes icons that could compliment 9 of the 12 major selling points for the Copper Vale Clinic Flow Platform software (the category titles are subject to change). The icons are not necessarily set in stone. For consistency with our presentation, the Protection, Integration, and Review icons should be used, but any of the remaining six (in particular, the Personalized icon) can be changed to whatever you think might be more suitable. The PSD also has some preliminary text for a few of the 12 selling points (we are refining the text now and will get the final content to designers very soon). Also note that the font is simply a placeholder; use whatever font you think would best compliment your design. Finally, keep in mind that the PSD does NOT reflect a design we are looking for; in fact, we hate this "design" and hesitate to call it a design. It was simply a way to arrange the elements to easily distribute them to designers.

We want an 8 1/2in x 11in 8-page flyer that is professional, simple, and has a clear message: this product will revolutionize your practice! We of course also need a website design that compliments the flyer design once the flyer design is finalized and chosen.

We will be monitoring this project closely-- please ask any questions you have!
Updates

Target Market(s)

Physicians, technicians, and marketing personnel in the LASIK industry.

Industry/Entity Type

Software

Number of Pages Required

4 page

Font styles to use
Serif
Sans Serif

```html
<!DOCTYPE html>
<html lang="en">
<head>
<meta charset="utf-8">
<title>Copper Vale Systems – Clinic Flow Platform Flyer</title>
<link rel="stylesheet" href="https://fonts.googleapis.com/css2?family=Cinzel:wght@600;700&family=Montserrat:wght@400;500&display=swap">
<style>
  :root {
    --sky: #4fd0f2;
    --ink: #1c1c1e;
    --band: #2b2b2e;
    --paper: #ffffff;
    --accent: #d9f26a;
    --photo-light: #e6e9ec;
    --photo-mid: #c9d2da;
    --photo-warm: #e9d9cc;
  }
  * { box-sizing: border-box; margin: 0; padding: 0; }
  html, body { width: 932px; height: 1200px; overflow: hidden; background: var(--paper); }
  .flyer { position: relative; width: 932px; height: 1200px; background: var(--paper); font-family: "Montserrat", Arial, sans-serif; }
  .brand { position: absolute; left: 49px; top: 27px; display: flex; align-items: center; gap: 16px; }
  .brand-square { width: 87px; height: 87px; background: var(--band); border: 4px solid var(--paper); box-shadow: 0 1px 4px rgba(0,0,0,0.35); }
  .brand-name { font-family: "Cinzel", "Times New Roman", serif; font-weight: 600; font-size: 42px; letter-spacing: 4px; color: var(--ink); }
  .artwork { position: absolute; left: 0; top: 0; }
  .feature { position: absolute; color: var(--paper); }
  .feature-title { font-family: "Cinzel", "Times New Roman", serif; font-weight: 700; font-size: 16px; letter-spacing: 1.5px; margin-bottom: 9px; }
  .feature-body { font-size: 9.3px; line-height: 1.16; text-align: justify; }
  .highlight { color: var(--accent); }
  .feature--tools { left: 161px; top: 612px; width: 279px; }
  .feature--review { left: 161px; top: 771px; width: 279px; }
  .feature--word { left: 161px; top: 956px; width: 716px; }
  .performance { position: absolute; left: 518px; top: 650px; width: 374px; color: var(--ink); }
  .performance .feature-title { padding-left: 66px; font-size: 16.5px; margin-bottom: 12px; }
</style>
</head>
<body>
<main class="flyer">
  <header class="brand">
    <div class="brand-square"></div>
    <h1 class="brand-name">Copper Vale Systems</h1>
  </header>

  <svg class="artwork" width="932" height="1200" viewBox="0 0 932 1200">
    <defs>
      <linearGradient id="photoTone" x1="0" y1="0" x2="1" y2="0.4">
        <stop offset="0" stop-color="#c9d2da"/>
        <stop offset="0.35" stop-color="#e9d9cc"/>
        <stop offset="0.7" stop-color="#e6e9ec"/>
        <stop offset="1" stop-color="#c9d2da"/>
      </linearGradient>
    </defs>
    <rect class="header-rule" x="6" y="127" width="922" height="13" fill="var(--sky)"/>
    <rect class="hero-photo" x="0" y="140" width="928" height="822" fill="url(#photoTone)" role="img" aria-label="Photo of a patient looking into an eye examination instrument"/>
    <polygon class="feature-panel" fill="var(--sky)"
      points="0,547 73,547 112,590 151,549 403,549 458,606 458,940 880,940 928,965 928,1120 0,1120"/>
    <line class="timeline" x1="112" y1="590" x2="112" y2="1120" stroke="var(--paper)" stroke-width="5"/>
    <polygon class="performance-card" fill="var(--paper)" points="464,667 796,479 928,552 928,937 464,937"/>
    <polyline points="466,667 466,937 880,937 928,962" fill="none" stroke="var(--ink)" stroke-width="3"/>
    <line x1="796" y1="479" x2="796" y2="554" stroke="var(--sky)" stroke-width="4"/>
    <g class="icon-gauge">
      <circle cx="797" cy="592" r="35" fill="var(--sky)" stroke="var(--paper)" stroke-width="3"/>
      <circle cx="797" cy="592" r="39" fill="none" stroke="var(--sky)" stroke-width="2"/>
      <path d="M777 602 A21 21 0 1 1 817 602" fill="none" stroke="var(--paper)" stroke-width="4"/>
      <line x1="797" y1="597" x2="808" y2="583" stroke="var(--paper)" stroke-width="3" stroke-linecap="round"/>
      <circle cx="797" cy="597" r="3.5" fill="var(--paper)"/>
    </g>
    <g class="icon-growth">
      <circle cx="112" cy="652" r="37" fill="var(--paper)"/>
      <rect x="91" y="663" width="6" height="8" fill="var(--sky)"/>
      <rect x="100" y="657" width="6" height="14" fill="var(--sky)"/>
      <rect x="109" y="650" width="6" height="21" fill="var(--sky)"/>
      <rect x="118" y="643" width="6" height="28" fill="var(--sky)"/>
      <path d="M87 658 Q107 650 125 633" fill="none" stroke="var(--sky)" stroke-width="3.5"/>
      <polygon points="120,630 133,626 129,639" fill="var(--sky)"/>
    </g>
    <g class="icon-review">
      <circle cx="112" cy="803" r="37" fill="var(--paper)"/>
      <path d="M95 785 h34 a6 6 0 0 1 6 6 v20 a6 6 0 0 1 -6 6 h-14 l-9 9 v-9 h-11 a6 6 0 0 1 -6 -6 v-20 a6 6 0 0 1 6 -6z" fill="var(--sky)"/>
      <g fill="var(--paper)" font-size="10" font-family="Arial, sans-serif" text-anchor="middle">
        <text x="106" y="798">★</text><text x="118" y="798">★</text>
        <text x="100" y="811">★</text><text x="112" y="811">★</text><text x="124" y="811">★</text>
      </g>
    </g>
    <g class="icon-thumbs">
      <circle cx="112" cy="990" r="37" fill="var(--paper)"/>
      <rect x="94" y="986" width="8" height="20" rx="1.5" fill="var(--sky)"/>
      <path d="M105 986 l8 -14 a4 4 0 0 1 7 3 l-2 9 h10 a4 4 0 0 1 4 5 l-3 14 a4 4 0 0 1 -4 3 h-20z" fill="var(--sky)"/>
    </g>
    <rect class="footer-band" x="0" y="1130" width="928" height="62" fill="var(--band)"/>
  </svg>

  <section class="feature feature--tools">
    <h2 class="feature-title">Improvement Tools</h2>
    <p class="feature-body">In the digital age our industry still requires patients to fill out forms with pen and paper which in turn have to be entered into a database by hand. Technicians must take digital information from (device), print it out into physical paper, then enter the data back into digital format. We say, “No more.” With the Copper Vale Clinic Flow Platform your practice will enjoy full digital <span class="highlight">integration</span> of all key equipment, including the laser, the Wavefront, and the HIPAA-compliant databases that connect them.</p>
  </section>

  <section class="feature feature--review">
    <h2 class="feature-title">Review</h2>
    <p class="feature-body">In the digital age our industry still requires patients to fill out forms with pen and paper which in turn have to be entered into a database by hand. Technicians must take digital information from (device), print it out into physical paper, then enter the data back into digital format. We say, “No more.” With the Copper Vale Clinic Flow Platform your practice will enjoy full digital <span class="highlight">integration</span> of all key equipment, including the laser, the Wavefront, and the HIPAA-compliant databases that connect them.</p>
  </section>

  <section class="feature feature--word">
    <h2 class="feature-title">Word of Mouth</h2>
    <p class="feature-body">In the digital age our industry still requires patients to fill out forms with pen and paper which in turn have to be entered into a database by hand. Technicians must take digital information from (device), print it out into physical paper, then enter the data back into digital format. We say, “No more.” With the Copper Vale Clinic Flow Platform your practice will enjoy full digital <span class="highlight">integration</span> of all key equipment, including the laser, the Wavefront, and the HIPAA-compliant databases that connect them.</p>
  </section>

  <section class="performance">
    <h2 class="feature-title">High Performance</h2>
    <p class="feature-body">It’s time for a revolution in an industry that depends on effective marketing, tracking marketing campaign effectiveness, and converting interest into procedures. Finally comes the solution: the Copper Vale Clinic Flow Platform which includes connectivity between your marketing records and your patient records. Two databases, one for patients and one for prospective patients, with a single program connecting them. It’s simple, it’s HIPAA-compliant, and it’s only the beginning.</p>
  </section>
</main>
</body>
</html>
```